Here is the link where the current banner is featured https://www.brimkit.com.au/collections/gel-blasters

I need the banner recreated into desktop and mobile format size.
Update the key points to:
- FREE SHIPPING AUSTRALIA WIDE
- SAME DAY DISPATCH
- BEST PRICE GUARANTEE
- 3000+ 5 STAR REVIEWS
- BEST SERVICE & WARRANTY
- 100% SECURE CHECKOUT

I want the banner to suit the style of the website and make it look better than the last graphic.

I also need the "save even more" picture to be recreated as it looks very plain at the moment,

```html
<!DOCTYPE html>
<html lang="en">
<head>
<meta charset="utf-8">
<title>Brimkit – Why Shop With Us</title>
<link rel="stylesheet" href="https://fonts.googleapis.com/css2?family=Oswald:wght@500&display=swap">
<style>
  :root {
    --night: #0b0b0b;
    --forest-mid: #3a3a3a;
    --blood: #7e1517;
    --blood-bright: #d3232b;
    --bone: #fbeee8;
    --white: #ffffff;
  }
  html, body {
    margin: 0;
    padding: 0;
    overflow: hidden;
    background: var(--night);
  }
  .usp-banner {
    position: relative;
    width: 1200px;
    height: 188px;
    overflow: hidden;
    font-family: "Oswald", "Arial Narrow", sans-serif;
    font-weight: 500;
    color: var(--white);
  }
  .forest-backdrop {
    position: absolute;
    inset: 0;
    background:
      radial-gradient(ellipse 260px 120px at 690px 90px, rgba(120,120,120,.55), transparent 70%),
      radial-gradient(ellipse 200px 100px at 330px 80px, rgba(90,90,90,.35), transparent 70%),
      linear-gradient(180deg, #1b1b1b 0%, var(--forest-mid) 45%, #141414 100%);
  }
  .usp {
    position: absolute;
    top: 0;
    width: 180px;
    height: 188px;
    transform: translateX(-50%);
    text-align: center;
  }
  .usp__icon {
    position: absolute;
    left: 50%;
    transform: translateX(-50%);
  }
  .usp__label {
    position: absolute;
    left: 0;
    right: 0;
    top: 129px;
    font-size: 15.5px;
    line-height: 19px;
    letter-spacing: -0.2px;
    text-transform: uppercase;
  }
  .usp__label .accent {
    background: var(--blood-bright);
    padding: 0 2px;
    font-size: 17px;
  }
  .splatter { fill: var(--blood); }
</style>
</head>
<body>
<section class="usp-banner" aria-label="Reasons to shop with Brimkit">
  <div class="forest-backdrop" role="img" aria-label="Dark misty pine forest"></div>

  <div class="usp" style="left:108px">
    <div class="usp__icon" style="top:25px;width:110px;height:130px" role="img" aria-label="Map of Australia on a red paint splash">
      <svg width="110" height="130" viewBox="0 0 110 130">
        <circle class="splatter" cx="55" cy="54" r="52"/>
        <rect class="splatter" x="50" y="90" width="8" height="38" rx="4"/>
      </svg>
    </div>
    <div class="usp__label"><span class="accent">Free</span> Shipping<br>Australia Wide</div>
  </div>

  <div class="usp" style="left:308px">
    <svg class="usp__icon" style="top:42px" width="56" height="56" viewBox="0 0 56 56" aria-hidden="true">
      <path d="M8 50 L46 12 M20 8 H48 V36" stroke="var(--bone)" stroke-width="7" fill="none" stroke-linecap="square"/>
    </svg>
    <div class="usp__label"><span class="accent">Same</span> Day<br>Dispatch</div>
  </div>

  <div class="usp" style="left:512px">
    <div class="usp__icon" style="top:28px;width:130px;height:150px" role="img" aria-label="Red paint splash">
      <svg width="130" height="150" viewBox="0 0 130 150">
        <ellipse class="splatter" cx="66" cy="66" rx="58" ry="54"/>
        <ellipse class="splatter" cx="44" cy="118" rx="30" ry="22"/>
      </svg>
    </div>
    <svg class="usp__icon" style="top:47px" width="52" height="40" viewBox="0 0 52 40" aria-hidden="true">
      <path d="M4 20 L19 34 L48 5" stroke="var(--bone)" stroke-width="7" fill="none"/>
    </svg>
    <div class="usp__label">Best Price<br><span class="accent">Guarantee</span></div>
  </div>

  <div class="usp" style="left:696px">
    <svg class="usp__icon" style="top:50px" width="152" height="38" viewBox="0 0 152 38" aria-hidden="true">
      <g fill="var(--bone)">
        <circle cx="12" cy="19" r="12"/><circle cx="42" cy="19" r="14"/><circle cx="76" cy="19" r="19"/>
        <circle cx="110" cy="19" r="14"/><circle cx="140" cy="19" r="12"/>
      </g>
      <g fill="var(--night)">
        <polygon points="12,12 14,17 19,17 15,20 16.5,25 12,22 7.5,25 9,20 5,17 10,17"/>
        <polygon points="42,10 44.5,16.5 51,16.5 46,20.5 48,27 42,23 36,27 38,20.5 33,16.5 39.5,16.5"/>
        <polygon points="76,7 79.5,15.5 88,15.5 81,21 83.5,30 76,25 68.5,30 71,21 64,15.5 72.5,15.5"/>
        <polygon points="110,10 112.5,16.5 119,16.5 114,20.5 116,27 110,23 104,27 106,20.5 101,16.5 107.5,16.5"/>
        <polygon points="140,12 142,17 147,17 143,20 144.5,25 140,22 135.5,25 137,20 133,17 138,17"/>
      </g>
    </svg>
    <div class="usp__label"><span class="accent">3000+</span><br>5 Star Reviews</div>
  </div>

  <div class="usp" style="left:892px">
    <div class="usp__icon" style="top:22px;width:110px;height:110px" role="img" aria-label="Red paint splash">
      <svg width="110" height="110" viewBox="0 0 110 110"><circle class="splatter" cx="55" cy="55" r="52"/></svg>
    </div>
    <svg class="usp__icon" style="top:44px" width="60" height="66" viewBox="0 0 60 66" aria-hidden="true">
      <path d="M42 50 A24 24 0 1 1 48 22" stroke="var(--bone)" stroke-width="8" fill="none"/>
      <rect x="44" y="22" width="10" height="18" rx="3" fill="var(--bone)"/>
      <path d="M42 50 Q38 58 28 58" stroke="var(--bone)" stroke-width="4" fill="none"/>
      <rect x="20" y="54" width="12" height="8" rx="3" fill="var(--bone)"/>
    </svg>
    <div class="usp__label">Best <span class="accent">Service</span><br>&amp; Warranty</div>
  </div>

  <div class="usp" style="left:1096px">
    <svg class="usp__icon" style="top:30px" width="82" height="82" viewBox="0 0 82 82" aria-hidden="true">
      <path d="M4 24 V4 H78 V78 H4 V58" stroke="var(--bone)" stroke-width="5" fill="none"/>
      <circle cx="20" cy="41" r="14" fill="var(--bone)"/>
      <circle cx="17" cy="41" r="4" fill="var(--night)"/>
      <path d="M32 36 H76 L80 41 L76 46 H70 L67 50 L63 46 L59 50 L55 46 L51 50 L47 46 H32 Z" fill="var(--bone)"/>
    </svg>
    <div class="usp__label"><span class="accent">100%</span> Secure<br>Checkout</div>
  </div>
</section>
</body>
</html>
```